WHAT LIES BEYOND? Discovering the shape of days with the Silent Lamp

Creating a book that is about living a spiritual life. The book is about letting go of the materialistic world and finding happiness through self realisation and enlightenment. The contents page is below that gives an idea of what is contained in the book.

The book is based on the writings of the Sikhs - from India. But it is written in a universal way that is understandable to all.

CONTENTS
Living for a purpose
- Born to be original! Dying as a copy!
- My relationship with everything but me!
- What is my purpose?

Life as a human being!
- Stages of Life
- Five Weaknesses

What is driving our lives?
- Information overload?
- What are your drivers?
- Giving life meaning

You reap what you sow
- Is my destiny written?
- Good and bad actions
- Maya – the illusion and it’s three modes

Slow down and let go
- The mind in overdrive
- Being aware of our mental health
- Why Slow Down?

The Guidance of the Guru
- Why do I need a Guru?
- What the Guru gives you
- Gurbani – the Guru’s Words

Staying connected
- Repeating the Mantra
- Doing two things at once
- Remembering in times of difficulty

Cultivating virtues
- Theory vs Practice
- Virtues and true religion
- Some key virtues

The Mystical Creation
- Experiencing ecstasy
- Enlightenment and intuition
- Spiritual Transformation

Good Company
- How do my companions affect me?
- The company of Saintly people
- Obtaining the fruits that the Guru describes

Serving selflessly
- Serving is our purpose
- Being grateful
- Being generous

Ten things to change your life today

Target Market(s)

All those who want to learn about spirituality. We are targeting young and middle aged but not necessarily ruling out older demographic.

Requirements
Must have
• The book cover:

- exciting and intriguing
- theme is "what lies beyond" in this world
- some kind of lean towards enlightenment
Nice to have
• It is not essential but the cover could subtly show something about the Sikh faith. Can discuss this further if necessary.
Should not have
• Should not:

- look dull and boring
- don't want it to look like a Buddhism book

```html
<!DOCTYPE html>
<html lang="en">
<head>
<meta charset="utf-8">
<title>What Lies Beyond? — Book Cover</title>
<link rel="stylesheet" href="https://fonts.googleapis.com/css2?family=Montserrat:wght@500;700;800&display=swap">
<style>
  :root {
    --page: #e4e4e1;
    --ink-light: #ffffff;
    --deep-blue: #2b2f9e;
    --royal-blue: #3540b8;
    --teal: #2f7fa6;
    --ember: #ff6a2a;
    --flare: #e23a5a;
    --night: #141a52;
  }
  * { box-sizing: border-box; margin: 0; padding: 0; }
  html, body {
    width: 1200px;
    height: 853px;
    overflow: hidden;
    background: var(--page);
  }
  .canvas {
    position: relative;
    width: 1200px;
    height: 853px;
    background: var(--page);
  }
  .book-cover {
    position: absolute;
    left: 320px;
    top: 26px;
    width: 560px;
    height: 800px;
    overflow: hidden;
    color: var(--ink-light);
    font-family: "Montserrat", "Helvetica Neue", Arial, sans-serif;
    text-align: center;
  }
  .cover-artwork {
    position: absolute;
    inset: 0;
    background:
      radial-gradient(ellipse 40% 12% at 62% 52%, rgba(255,106,42,0.55), transparent 70%),
      linear-gradient(158deg, transparent 40%, rgba(226,58,90,0.55) 52%, rgba(255,106,42,0.35) 58%, transparent 68%),
      radial-gradient(ellipse 30% 60% at 12% 78%, rgba(47,127,166,0.75), transparent 70%),
      radial-gradient(ellipse 25% 50% at 38% 20%, rgba(47,127,166,0.55), transparent 70%),
      radial-gradient(ellipse 40% 40% at 80% 30%, rgba(53,64,184,0.9), transparent 75%),
      linear-gradient(180deg, var(--deep-blue), var(--night) 50%, var(--royal-blue));
  }
  .cover-label,
  .cover-author {
    position: absolute;
    left: 0;
    right: 0;
    font-size: 11px;
    font-weight: 700;
    letter-spacing: 0.01em;
    text-transform: uppercase;
  }
  .cover-label { top: 60px; }
  .cover-author { top: 746px; }
  .cover-title {
    position: absolute;
    left: 0;
    right: 0;
    top: 248px;
    font-size: 86px;
    font-weight: 800;
    line-height: 0.98;
    letter-spacing: 0.01em;
    text-transform: uppercase;
  }
  .cover-title span { display: block; }
  .cover-subtitle {
    position: absolute;
    left: 0;
    right: 0;
    top: 522px;
    font-size: 19px;
    font-weight: 500;
    line-height: 1.25;
  }
</style>
</head>
<body>
  <main class="canvas">
    <section class="book-cover">
      <div class="cover-artwork" role="img" aria-label="Abstract textured painting in deep blues and teal with a glowing orange and crimson diagonal streak and scattered ember flecks"></div>
      <p class="cover-label">Exciting and intriguing</p>
      <h1 class="cover-title">
        <span>What</span>
        <span>Lies</span>
        <span>Beyond?</span>
      </h1>
      <p class="cover-subtitle">Discovering the shape of days<br>with the Silent Lamp</p>
      <p class="cover-author">By: Arlen Voss</p>
    </section>
  </main>
</body>
</html>
```